Stationary and email footer design using existing Logo design

Using the Logo design I currently have I need now to have this applied to all stationary requirements including email footer, Letter Head and footer, envelopes both window and non window ( standard letter size ).
You previously did the Logo and business cards so that's good.

```html
<!DOCTYPE html>
<html lang="en">
<head>
<meta charset="utf-8">
<title>Violet Crest Letterhead</title>
<link href="https://fonts.googleapis.com/css2?family=Arimo:wght@400;700&display=swap" rel="stylesheet">
<style>
  :root {
    --backdrop: #d9dcde;
    --paper: #ffffff;
    --brand-purple: #8a67b8;
    --brand-purple-deep: #6f4aa3;
    --rule-grey: #b9bbbe;
    --body-text: #6e6e72;
    --muted: #8d8d92;
  }
  * { box-sizing: border-box; margin: 0; padding: 0; }
  html, body {
    width: 1200px; height: 784px; overflow: hidden;
    background: var(--backdrop);
    font-family: "Arimo", Arial, sans-serif;
  }
  .letterhead {
    position: absolute; left: 335px; top: 17px;
    width: 530px; height: 750px;
    background: var(--paper);
    box-shadow: 0 2px 10px rgba(0,0,0,0.12);
    overflow: hidden;
  }
  .corner-accent {
    position: absolute;
    background: linear-gradient(135deg, #a98bd0, #6f4aa3);
  }
  .corner-accent--top {
    right: 0; top: 0; width: 150px; height: 60px;
    clip-path: polygon(0 0, 100% 0, 100% 100%);
  }
  .corner-accent--bottom {
    left: 0; bottom: 0; width: 150px; height: 60px;
    clip-path: polygon(0 0, 100% 100%, 0 100%);
  }
  .masthead {
    position: absolute; left: 48px; top: 42px;
    display: flex; align-items: center; gap: 14px;
  }
  .brand {
    display: flex; align-items: center; gap: 7px;
    color: var(--brand-purple-deep);
    font-size: 15px; font-weight: 700; letter-spacing: 0.4px;
    line-height: 1.1;
  }
  .brand-mark { width: 12px; height: 12px; background: var(--brand-purple); }
  .divider { width: 1px; height: 48px; background: var(--rule-grey); }
  .contact { font-size: 6.5px; color: var(--muted); line-height: 1.6; }
  .contact .address { color: var(--brand-purple-deep); font-weight: 700; }
  .contact-row { display: flex; align-items: center; gap: 4px; white-space: nowrap; }
  .contact-row svg { width: 7px; height: 7px; flex: none; }
  .letter-body {
    position: absolute; left: 62px; top: 122px; width: 390px;
    font-size: 8.4px; line-height: 1.45; color: var(--body-text);
  }
  .letter-body p { margin-bottom: 11px; }
  .signature {
    position: absolute; left: 62px; top: 410px;
    width: 150px; height: 42px;
    background: linear-gradient(90deg, rgba(120,120,125,0.08), rgba(120,120,125,0.18), rgba(120,120,125,0.08));
    border-radius: 3px;
  }
</style>
</head>
<body>
  <div class="letterhead">
    <div class="corner-accent corner-accent--top" role="img" aria-label="Purple corner decoration"></div>
    <div class="corner-accent corner-accent--bottom" role="img" aria-label="Purple corner decoration"></div>

    <header class="masthead">
      <div class="brand"><span class="brand-mark"></span>Violet Crest<br>Financial Planners</div>
      <div class="divider"></div>
      <div class="contact">
        <div class="contact-row address">
          <svg viewBox="0 0 10 10"><path d="M5 0.5a3.3 3.3 0 0 0-3.3 3.3C1.7 6.3 5 9.5 5 9.5s3.3-3.2 3.3-5.7A3.3 3.3 0 0 0 5 0.5z" fill="var(--brand-purple)"/></svg>
          Suite 4, Level 2 Harbour Point, 12 Wattle Road, Northbay WA 6100
        </div>
        <div class="contact-row">
          <svg viewBox="0 0 10 10"><circle cx="5" cy="5" r="4.5" fill="var(--brand-purple)"/></svg>
          08 5550 1234 &nbsp; hello@violetcrest.example
        </div>
        <div class="contact-row">
          <svg viewBox="0 0 10 10"><circle cx="5" cy="5" r="4.5" fill="var(--brand-purple)"/></svg>
          www.violetcrest.example
        </div>
      </div>
    </header>

    <main class="letter-body">
      <p>Lorem Ipsum is simply dummy text of the printing and typesetting industry. Lorem Ipsum has been the industry's standard dummy text ever since the 1500s, when an unknown printer took a galley of type and scrambled it to make a type specimen book. It has survived not only five centuries, but also the leap into electronic typesetting, remaining essentially unchanged. It was popularised in the 1960s with the release of transfer lettering sheets containing Lorem Ipsum passages, and more recently with page layout software including versions of Lorem Ipsum.</p>
      <p>It is a long established fact that a reader will be distracted by the readable content of a page when looking at its layout. The point of using Lorem Ipsum is that it has a more-or-less normal distribution of letters, as opposed to using 'Content here, content here', making it look like readable English. Many desktop publishing packages and web page editors now use Lorem Ipsum as their default model text, and a search for 'lorem ipsum' will uncover many web sites still in their infancy. Various versions have evolved over the years, sometimes by accident, sometimes on purpose (injected humour and the like).</p>
      <p>Contrary to popular belief, Lorem Ipsum is not simply random text. It has roots in a piece of classical Latin literature from 45 BC, making it over 2000 years old. A language scholar at a small regional college looked up one of the more obscure Latin words, consectetur, from a Lorem Ipsum passage, and going through the cites of the word in classical literature, discovered the undoubtable source. Lorem Ipsum comes from sections 1.10.32 and 1.10.33 of an old treatise on ethics, using its structures to generate Lorem Ipsum which looks reasonable. The generated Lorem Ipsum is therefore always free from repetition, injected humour, or non-characteristic words etc.</p>
    </main>

    <div class="signature" role="img" aria-label="Handwritten signature of the sender"></div>
  </div>
</body>
</html>
```